Essential Oil Blend Label Design

I need a label designed for our stress relief essential blend, Marlo's Drift.
The text for the front of the logo will be as follows:
"Marlo's Drift
All Natural Stress and Anxiety Relief
www.corvantglow.com"
Please make the front text small enough that it will show up in a picture of the bottle with the label is applied without being cut off on the edges. For reference, the label will be 4" x 2" and will go on these bottles:
http://www.brindlevessel.com/glass-bottles/european-dropper/amber/30ml-kqt30
On one of the sides of the label I would like this text, going up the label so that you turn the bottle sideways to read it (like in the attached label):
"Contains a pure, undiluted essential oil blend"
On the other side "For use in aromatherapy"
I would like this label to incorporate elements of a lush, green garden, like the Garden of Eden. The goal is for it convey peace and relaxation.
Please also note that I have attached the label for our other product for reference. The new label should be similar in its basic design as far as where the text is present and the overall style. My one problem with the attached label, though, is that the front text is a little too large and doesn't show up all the way in a picture. (I've attached the picture of the bottle as well so you can see what I mean).
I look forward to working with you!
Neil

```html
<!DOCTYPE html>
<html lang="en">
<head>
<meta charset="utf-8">
<title>Marlo's Drift – Essential Oil Label</title>
<link rel="stylesheet" href="https://fonts.googleapis.com/css2?family=Arvo:wght@700&family=Lobster+Two:ital,wght@1,700&family=Niconne&family=Tinos:wght@400;700&display=swap">
<style>
  :root {
    --backdrop: #8e8f93;
    --label-aqua: #b6e3dc;
    --forest: #0a6a3a;
    --forest-band: #086a3b;
    --lime: #a7d33c;
    --pill-fill: #ddf3ee;
    --ink: #1e1e1e;
    --cream: #eef4dc;
    --white: #ffffff;
  }
  * { box-sizing: border-box; margin: 0; padding: 0; }
  html, body { width: 1200px; height: 1200px; overflow: hidden; }
  body { background: var(--backdrop); position: relative; }

  .label {
    position: absolute;
    left: 50px; top: 323px;
    width: 1100px; height: 553px;
    background: var(--label-aqua);
    overflow: hidden;
  }
  .label__top-band {
    position: absolute; left: 0; top: 0; width: 100%; height: 10px;
    background: var(--lime);
  }
  .label__tagline {
    position: absolute; left: 0; top: 22px; width: 100%;
    text-align: center;
    font-family: "Lobster Two", cursive;
    font-style: italic; font-weight: 700;
    font-size: 28px; color: var(--forest);
  }
  .label__garden {
    position: absolute; left: 276px; top: 118px;
    width: 552px; height: 250px;
  }
  .label__name {
    position: absolute; left: 338px; top: 71px;
    width: 424px; height: 64px;
    border: 3px solid var(--lime);
    border-radius: 22px;
    background: var(--pill-fill);
    display: flex; align-items: center; justify-content: center;
    font-family: "Arvo", serif; font-weight: 700;
    font-size: 44px; color: var(--forest);
  }
  .label__url {
    position: absolute; left: 0; top: 374px; width: 100%;
    text-align: center;
    font-family: "Tinos", serif; font-size: 26px; color: var(--ink);
  }
  .label__claim-band {
    position: absolute; left: 0; top: 417px; width: 100%; height: 116px;
    background: var(--forest-band);
    text-align: center;
  }
  .label__claim {
    margin-top: 12px;
    font-family: "Niconne", cursive;
    font-size: 44px; line-height: 1; color: var(--cream);
    letter-spacing: 1px;
  }
  .label__use {
    margin-top: 6px;
    font-family: "Tinos", serif;
    font-size: 31px; line-height: 1; color: var(--white);
  }
  .label__bottom-band {
    position: absolute; left: 0; bottom: 0; width: 100%; height: 20px;
    background: var(--lime);
  }
  .side-copy {
    position: absolute;
    width: 321px; height: 140px;
    font-family: "Tinos", serif;
    font-size: 16.5px; line-height: 27px;
    color: var(--ink);
    text-align: justify;
    text-align-last: left;
  }
  .side-copy strong { font-weight: 700; }
  .side-copy--left {
    left: -15px; top: 148px;
    transform: rotate(90deg);
  }
  .side-copy--right {
    left: 799px; top: 148px;
    transform: rotate(-90deg);
  }
</style>
</head>
<body>
  <div class="label">
    <div class="label__top-band"></div>
    <p class="label__tagline">All Natural Stress and Anxiety Relief</p>

    <svg class="label__garden" viewBox="0 0 552 250" role="img" aria-label="Watercolour garden scene with lush green plants and pink and purple flowers">
      <defs>
        <linearGradient id="gardenTone" x1="0" y1="0" x2="0" y2="1">
          <stop offset="0" stop-color="#9fd3e0"/>
          <stop offset="0.35" stop-color="#8cc97a"/>
          <stop offset="0.7" stop-color="#5fae45"/>
          <stop offset="1" stop-color="#a6d66a"/>
        </linearGradient>
      </defs>
      <ellipse cx="276" cy="125" rx="276" ry="125" fill="url(#gardenTone)"/>
    </svg>

    <div class="label__name">Marlo's Drift</div>

    <p class="label__url">www.corvantglow.com</p>

    <div class="label__claim-band">
      <p class="label__claim">Contains A Pure, Undiluted Essential Oil Blend</p>
      <p class="label__use">For use in aromatherapy</p>
    </div>
    <div class="label__bottom-band"></div>

    <p class="side-copy side-copy--left"><strong>Corvant Glow</strong> is the most effective all natural pain reliever available today—we guarantee it. Made from a blend of seventeen different essential oils, each one chosen for their proven</p>

    <p class="side-copy side-copy--right"><strong>Corvant Glow</strong> is the most effective all natural pain reliever available today—we guarantee it. Made from a blend of seventeen different essential oils, each one chosen for their proven anti-inflammatory and pain relieving properties, Corvant Glow quickly</p>
  </div>
</body>
</html>
```